Lindenhof Köln, Greta Wommer sucht Design
Zielgruppe
Ich mache:
1. (lebendige) Stadtführungen bzw. Gästeführung in jeder Hinsicht -> in Köln für kleine und große Gruppen und vielfältige, individuelle Themen (bei größeren Gruppen setze ich zusätzliche Guides ein, so dass ich Veranstaltungen bis 300 Personen managen kann)
2. VIP-Gästebetreuung
3. 'Rundum-Sorglos-Pakete' = komplette Eventplanung und -durchführung, d. h. Programmerstellung nach Anzahl Teilnehmer, Budget und Zeitrahmen, einschließlich Auswahl Restaurants etc. und ggfls. Bereitstellung von Limousinen, Bussen oder anderen Fahrzeugen
4. Stadtrundfahrten (dazu biete ich Fahrzeuge unterschiedlicher Größe an, oder steige als Tour-Guide in den vorhandenen Bus einer Gruppe für die Stadtrundfahrt zu)
5. Schiffstouren
6. Komplett-Planung und Durchführung von Rahmen- oder Partnerprogrammen für Firmen, deren Kunden, Mitarbeiter oder Gäste am Rande einer Tagung, Konferenz etc. unterhalten werden sollen (z. B. eine Stadtführung nach der Konferenz und vor dem Abendessen)
7. Auch Halbtages- oder Ganztagesprogramme
Zielgruppe:
Ich arbeite zwar sehr viel für private Gruppe, die möchte ich unbedingt weiterhin ansprechen, aber zunehmend auch Firmen, da ich im Bereich der VIP-Gästebetreuung und 'Rundum-Sorglos-Planung' auf zahlreiche, sehr namhafte Referenzen verweisen kann.
a) Private Gruppen (für herkömmliche Stadtführung, -rundfahrt, Schiffstour im Rahmen von diversen Anlässen)
b) Firmen (für Kundenveranstaltungen, Firmenfeiern, Rahmenprogramm während Konferenz etc., Partnerprogramm (d. h. während die Konferenzteilnehmer tagen, kümmere ich mich um die mitgereisten Partner)
c) große namhafte Hotels, die ihren Gästen eine Gästeführerin vermitteln möchten
Aufgabenstellung
Ich wünsche mir, dass aus dem Logo hervorgeht, dass ich (zertifizierte) Stadtführerin (=Gästeführerin) in Köln bin und lege Wert darauf, dass mein Design vor allem Kompetenz, Professionalität, Innovation und Vertrauen ausstrahlt.
Bei Stadtführern in Köln findet sich im Logo meist der Kölner Dom (wie bei mir aktuell auch) oder das Stadtwappen Kölns, das schwarz-weiß-rot ist. Das Stadtwappen möchte ich auf KEINEN Fall, der Dom ist immer gut aber nicht zwingend.
Auf meiner Website www.lindenhof-koeln.de habe ich mit den Farben schwarz, weinrot und grau gearbeitet. Das gefällt mir noch immer, ist aber nicht in Stein gemeißelt. Ich bevorzuge auf jeden Fall KLARE Farben und ein KLARES Design. Eher minimalistisch als verschnörkelt.

```html
<!DOCTYPE html>
<html lang="de">
<head>
<meta charset="utf-8">
<title>Lindenhof – Geschäftsausstattung</title>
<link rel="stylesheet" href="https://fonts.googleapis.com/css2?family=Arimo:wght@400;700&display=swap">
<style>
  :root {
    --brand-red: #d11418;
    --ink: #111111;
    --paper: #ffffff;
    --card: #f6f5f3;
    --backdrop: #e9e9ea;
    --shadow: rgba(0,0,0,0.12);
  }
  * { box-sizing: border-box; margin: 0; padding: 0; }
  html, body { width: 1200px; height: 800px; overflow: hidden; }
  body {
    background: var(--backdrop);
    font-family: "Arimo", Arial, sans-serif;
    color: var(--ink);
    position: relative;
  }

  /* Letterhead (A4) */
  .letterhead {
    position: absolute; left: 60px; top: 28px;
    width: 523px; height: 744px;
    background: var(--paper);
    box-shadow: 0 2px 10px var(--shadow);
  }
  .fold-mark {
    position: absolute; left: 0; top: 262px;
    width: 12px; height: 1px; background: var(--brand-red);
  }
  .letter-brand {
    position: absolute; right: 58px; top: 40px; width: 120px;
  }
  .brand-mark {
    display: flex; align-items: center; gap: 5px;
  }
  .brand-dot { border-radius: 50%; background: var(--brand-red); flex: none; }
  .brand-name { font-weight: 700; color: var(--ink); line-height: 1; }
  .brand-tagline { font-size: 4px; margin-top: 1px; }
  .letter-brand .brand-dot { width: 18px; height: 18px; }
  .letter-brand .brand-name { font-size: 12px; }
  .letter-brand .brand-tagline { margin-left: 23px; }
  .info-block { font-size: 6px; line-height: 1.35; margin-top: 10px; margin-left: 23px; }
  .info-block strong { font-weight: 700; }

  .sender-line {
    position: absolute; left: 58px; top: 150px;
    font-size: 6.5px; word-spacing: 2px;
  }
  .sender-line span + span { margin-left: 8px; }
  .recipient {
    position: absolute; left: 58px; top: 166px;
    font-size: 9.5px; line-height: 1.22;
  }
  .letter-date {
    position: absolute; right: 58px; top: 196px;
    font-size: 6.5px; line-height: 1.3; width: 80px;
  }
  .letter-date strong { display: block; font-weight: 700; }
  .salutation {
    position: absolute; left: 58px; top: 268px; font-size: 9.5px;
  }
  .letter-body {
    position: absolute; left: 58px; top: 296px; width: 400px;
    font-size: 9.5px; line-height: 1.42;
  }
  .page-number {
    position: absolute; right: 58px; bottom: 54px; width: 80px;
    font-size: 6.5px; line-height: 1.3;
  }
  .page-number strong { display: block; font-weight: 700; }

  /* Business cards (85 × 55) */
  .business-card {
    position: absolute; width: 340px; height: 220px;
    background: var(--card);
    box-shadow: 0 2px 8px var(--shadow);
  }
  .card-front { left: 720px; top: 90px; }
  .card-back { left: 720px; top: 400px; }

  .card-front .front-mark {
    position: absolute; left: 0; right: 0; top: 26px;
    display: flex; flex-direction: column; align-items: center;
  }
  .card-front .brand-dot { width: 104px; height: 104px; }
  .card-front .brand-name { font-size: 27px; margin-top: 14px; }
  .card-front .brand-tagline { font-size: 11px; margin-top: 3px; }

  .card-back .back-mark {
    position: absolute; left: 30px; top: 28px;
  }
  .card-back .brand-dot { width: 34px; height: 34px; }
  .card-back .brand-name { font-size: 15px; }
  .card-back .brand-tagline { font-size: 5.5px; margin-left: 39px; }
  .card-back .holder {
    position: absolute; left: 69px; top: 96px;
    font-size: 10px; line-height: 1.3;
  }
  .card-back .holder strong { font-weight: 700; }
</style>
</head>
<body>

<article class="letterhead">
  <span class="fold-mark"></span>

  <header class="letter-brand">
    <div class="brand-mark">
      <span class="brand-dot"></span>
      <span class="brand-name">Lindenhof</span>
    </div>
    <p class="brand-tagline" style="margin-left:23px">Greta Wommer führt in Köln</p>
    <p class="info-block"><strong>Greta Wommer</strong><br>Zertifizierte Gästeführerin<br>DIN EN 155</p>
    <p class="info-block"><strong>Adresse</strong><br>Lindgasse 7<br>50667 Köln</p>
  </header>

  <p class="sender-line"><span>Greta Wommer</span><span>Lindgasse 7</span><span>50667 Köln</span></p>
  <address class="recipient" style="font-style:normal">
    Firma<br>Max Mustermann<br>Beispielstraße 23a<br>12345 Berlin
  </address>
  <p class="letter-date"><strong>Datum</strong>12 Mai 2017</p>

  <p class="salutation">Sehr geehrter Herr Mustermann,</p>
  <p class="letter-body">Lorem ipsum dolor sit amet, consetetur sadipscing elitr, sed diam nonumy eirmod tempor invidunt ut labore et dolore magna aliquyam erat, sed diam voluptua. At vero eos et accusam et justo duo dolores et ea rebum. Stet clita kasd gubergren, no sea takimata sanctus est Lorem ipsum dolor sit amet. Lorem ipsum dolor sit amet, consetetur sadipscing elitr, sed diam nonumy eirmod tempor invidunt ut labore et dolore magna aliquyam erat, sed diam voluptua. At vero eos et accusam et justo duo dolores et ea rebum. Stet clita kasd gubergren, no sea takimata sanctus est Lorem ipsum dolor sit amet.</p>

  <p class="page-number"><strong>Seite</strong>1 von 1</p>
</article>

<section class="business-card card-front">
  <div class="front-mark">
    <span class="brand-dot"></span>
    <span class="brand-name">Lindenhof</span>
    <p class="brand-tagline">Greta Wommer führt in Köln</p>
  </div>
</section>

<section class="business-card card-back">
  <div class="back-mark">
    <div class="brand-mark">
      <span class="brand-dot"></span>
      <span class="brand-name">Lindenhof</span>
    </div>
    <p class="brand-tagline">Greta Wommer führt in Köln</p>
  </div>
  <p class="holder"><strong>Greta Wommer</strong><br>Zertifizierte Gästeführerin<br>DIN EN 155</p>
</section>

</body>
</html>
```